Annual Report concept for Government Infrastructure project

Brief:

We are seeking a design concept for our annual report. We would like the front cover, contents pages, as well as 1 double-page spread (so 5 pages all up) within this contest.

This year's report needs to be in B5 size (176 x 250mm / 6.93 x 9.84 inches).

Last year was our first Annual Report and the company was in its early stages. We've progressed a lot and while the old design is quite static, we'd like the new design to have a sense of progress. It should look contemporary and innovative.

Please note that the report is being split into two parts; (1) the layout design (this contest) and (2) the completion of the full report (a follow up project with the winning designer at an agreed budget).

Attached is is last year's version for reference (your can use the content of this within your Cover, Contents, and double-page spread), as well as our branding guidelines.

About our company:

Tarrowdale Freightlink Company Limited (TFC) was established to facilitate the development of an intermodal terminal at Moorebank in Sydney’s south-west.

TFC is a government business enterprise, wholly owned by the Velmoran Crown Authority. TFC aims to optimise private sector expertise and investment, through a competitive process, to develop and operate the intermodal terminal and meet the project’s objectives.

```html
<!DOCTYPE html>
<html lang="en">
<head>
<meta charset="utf-8">
<title>Onward Progress — Annual Report 2014</title>
<link href="https://fonts.googleapis.com/css2?family=Oswald:wght@200;300;400&display=swap" rel="stylesheet">
<style>
  :root {
    --page-bg: #f2f2f0;
    --teal: #1fa6a6;
    --white: #ffffff;
    --photo-light: #a39a90;
    --photo-mid: #6f665d;
    --photo-dark: #2e2925;
  }
  * { margin: 0; padding: 0; box-sizing: border-box; }
  html, body {
    width: 1005px;
    height: 1200px;
    overflow: hidden;
    background: var(--page-bg);
  }
  .book {
    position: absolute;
    left: 115px;
    top: 50px;
    width: 774px;
    height: 1100px;
    display: flex;
    font-family: "Oswald", sans-serif;
    color: var(--white);
  }
  .spine {
    width: 56px;
    height: 100%;
    background: var(--teal);
    display: flex;
    flex-direction: column;
    align-items: center;
    padding: 40px 0;
    writing-mode: vertical-rl;
  }
  .spine-title {
    font-weight: 400;
    font-size: 22px;
    letter-spacing: 2px;
    text-transform: uppercase;
  }
  .spine-caption {
    margin-top: 360px;
    font-weight: 400;
    font-size: 16px;
    letter-spacing: 1px;
  }
  .cover {
    position: relative;
    width: 718px;
    height: 100%;
    overflow: hidden;
  }
  .cover-photo {
    position: absolute;
    inset: 0;
    background:
      radial-gradient(ellipse at 30% 20%, rgba(255,255,255,0.16), transparent 55%),
      radial-gradient(ellipse at 85% 60%, rgba(0,0,0,0.35), transparent 60%),
      linear-gradient(165deg, var(--photo-light) 0%, var(--photo-mid) 50%, var(--photo-dark) 100%);
  }
  .cover-title {
    position: absolute;
    left: 70px;
    top: 420px;
    font-weight: 200;
    text-transform: uppercase;
    line-height: 1;
  }
  .title-line {
    display: block;
    width: 500px;
    font-size: 118px;
    letter-spacing: 1px;
    padding-bottom: 6px;
    border-bottom: 4px solid var(--teal);
  }
  .title-line + .title-line { margin-top: 8px; }
  .cover-subtitle {
    position: absolute;
    left: 72px;
    top: 705px;
    font-weight: 300;
    font-size: 24px;
    letter-spacing: 10px;
    text-transform: uppercase;
  }
  .brand {
    position: absolute;
    left: 455px;
    top: 880px;
    display: flex;
    align-items: center;
    gap: 14px;
  }
  .brand-mark { width: 58px; height: 58px; }
  .brand-name {
    font-weight: 300;
    font-size: 18px;
    line-height: 1.1;
    letter-spacing: 1.5px;
    text-transform: uppercase;
  }
</style>
</head>
<body>
  <main class="book">
    <aside class="spine">
      <span class="spine-title">Onward Progress</span>
      <span class="spine-caption">Tarrowdale Freightlink Company Annual Report 2014</span>
    </aside>

    <section class="cover">
      <div class="cover-photo" role="img" aria-label="Sepia-toned close-up photograph of railway tracks with sleepers and ballast stretching into the distance"></div>

      <h1 class="cover-title">
        <span class="title-line">Onward</span>
        <span class="title-line">Progress</span>
      </h1>
      <p class="cover-subtitle">Annual Report 2014</p>

      <div class="brand">
        <svg class="brand-mark" viewBox="0 0 58 58" aria-hidden="true">
          <circle cx="29" cy="29" r="27" fill="var(--white)"/>
        </svg>
        <p class="brand-name">Tarrowdale<br>Freightlink<br>Company</p>
      </div>
    </section>
  </main>
</body>
</html>
```